Harbor Business Cards

I need a business card designed with the following information.

Company Name: Harbor Wealth Management
Name: BriAnne Dockery
Title: Executive Assistant
Cell: (281) 555-0173
Direct Line: (832) 555-0148
Email: brianne@harborwmx.com
Address: 20537 W. Marlowe PKWY Ste. B
Ashford, Ok 77390

I have attached the logo.
I would like it in navy blue and silver.
Thanks.

```html
<!DOCTYPE html>
<html lang="en">
<head>
<meta charset="utf-8">
<title>Harbor Wealth Management – Business Card</title>
<link href="https://fonts.googleapis.com/css2?family=Work+Sans:wght@300;400;500;600&display=swap" rel="stylesheet">
<style>
  :root {
    --navy: #16223d;
    --silver-bg: #d4d6d9;
    --card: #ffffff;
    --text-grey: #5a5d63;
    --shadow: rgba(0,0,0,0.22);
  }
  * { box-sizing: border-box; margin: 0; padding: 0; }
  html, body { width: 1200px; height: 1000px; overflow: hidden; }
  body {
    background: var(--silver-bg);
    font-family: "Work Sans", Arial, sans-serif;
    color: var(--navy);
    position: relative;
  }
  .card {
    position: absolute;
    left: 273px;
    width: 654px;
    height: 372px;
    background: var(--card);
    box-shadow: 0 6px 14px var(--shadow);
    overflow: hidden;
  }
  .card--front { top: 108px; }
  .card--back { top: 518px; }

  .brand { position: absolute; text-align: center; color: var(--navy); font-weight: 400; }
  .brand__mark { width: 36px; height: 36px; background: var(--navy); margin: 0 auto 22px; }
  .brand__name { font-size: 28px; letter-spacing: 14px; margin-right: -14px; line-height: 1; }
  .brand__sub { font-size: 10px; letter-spacing: 4px; margin-right: -4px; margin-top: 10px; }

  .card--front .brand { left: 70px; width: 230px; top: 150px; }

  .divider {
    position: absolute; left: 320px; top: 84px; width: 2px; height: 174px;
    background: var(--navy);
  }
  .details { position: absolute; left: 345px; top: 82px; }
  .details__name { font-size: 24px; font-weight: 500; letter-spacing: 2px; line-height: 1; }
  .details__title { font-size: 15px; font-weight: 500; color: var(--text-grey); letter-spacing: 0.6px; margin-top: 10px; }
  .details__address { font-size: 14.5px; font-weight: 300; color: var(--text-grey); margin-top: 16px; line-height: 17px; }
  .contact-list { list-style: none; margin-top: 14px; }
  .contact-list li {
    display: flex; align-items: center; font-size: 14.5px; font-weight: 300;
    color: var(--text-grey); height: 20px;
  }
  .contact-list svg { width: 10px; height: 10px; margin-right: 10px; fill: none; stroke: var(--navy); stroke-width: 1.6; }

  .web-band {
    position: absolute; right: 0; bottom: 0; width: 318px; height: 27px;
    background: var(--navy);
    clip-path: polygon(16px 0, 100% 0, 100% 100%, 0 100%);
    color: #fff; font-size: 14px; font-weight: 300;
    display: flex; align-items: center; padding-left: 84px;
  }
  .web-band b, .web b { font-weight: 600; }

  .card--back .brand { left: 0; width: 100%; top: 120px; }
  .card--back .brand__mark { width: 46px; height: 46px; margin-bottom: 26px; }
  .card--back .brand__name { font-size: 36px; letter-spacing: 18px; margin-right: -18px; }
  .card--back .brand__sub { font-size: 13px; letter-spacing: 5px; margin-right: -5px; margin-top: 14px; }

  .web {
    position: absolute; left: 0; width: 100%; top: 336px; text-align: center;
    font-size: 14.5px; font-weight: 300; color: var(--navy);
  }
</style>
</head>
<body>
  <section class="card card--front">
    <div class="brand">
      <div class="brand__mark"></div>
      <div class="brand__name">HARBOR</div>
      <div class="brand__sub">WEALTH MANAGEMENT</div>
    </div>
    <div class="divider"></div>
    <div class="details">
      <h1 class="details__name">BRIANNE DOCKERY</h1>
      <p class="details__title">Executive Assistant</p>
      <p class="details__address">20537 W. Marlowe Pkwy Ste.<br>B Ashford, Ok 77390</p>
      <ul class="contact-list">
        <li><svg viewBox="0 0 10 10"><path d="M2 1 L4 1 L4.5 3 L3.3 4 Q4.3 6 6 6.7 L7 5.5 L9 6 L9 8 Q5 9.5 1 4 Z"/></svg>(281) 555-0173</li>
        <li><svg viewBox="0 0 10 10"><rect x="2.5" y="0.8" width="5" height="8.4" rx="0.8"/><line x1="4.3" y1="7.6" x2="5.7" y2="7.6"/></svg>(832) 555-0148</li>
        <li><svg viewBox="0 0 10 10"><rect x="0.8" y="2" width="8.4" height="6"/><path d="M0.8 2 L5 5.3 L9.2 2"/></svg>brianne@harborwmx.com</li>
      </ul>
    </div>
    <div class="web-band">www.<b>BriAnneDockery</b>.com</div>
  </section>

  <section class="card card--back">
    <div class="brand">
      <div class="brand__mark"></div>
      <div class="brand__name">HARBOR</div>
      <div class="brand__sub">WEALTH MANAGEMENT</div>
    </div>
    <p class="web">www.<b>harborwealthmanagement</b>.com</p>
  </section>
</body>
</html>
```